Simple design for eCommerce retailer of Custom Cut Mirror Frames

We need a fresh design for our eCommerce store. Currently, we need a design for each page on the existing site.

Here is the site as it stands right now: glassvela.com

Here is a competitor site that we like. The owner really likes the block look for the home page: framorly.com

Here is a video we would like to feature: https://videohost.example/v/Kp7rTq2LmXa

Here is the color palate, emphasis on the green and purple: https://palettes.example/quiet-bay-theme-48271953/?showPublished=true

Here is an example of a landing page we are currently using: https://glassvela.com/lander-10-off-install/

Font for the site should be the google font Lato

Home page should include the following sections/blocks:

How it works
Shop now
Testimonials
Featured Products
Before and After Gallery
Updates

My team has been slow getting back to me with feedback. I'm pushing them to speed their process up.

Target Market(s)

Women, Ages 35-65+

Number of Pages Required

5+ page

Font styles to use
Sans Serif

Requirements
Must have
• -Before and after gallery
• -Star ratings
• -eCommerce look and feel
• -Info about being able to order free samples
• -Language from the checkmarks on the landing page
• -sleek product page
• -home page should be have a very modern design feel
Should not have
• Product Prices...the user has to use the calculator to determine the price of their purchase.
• Sliders

```html
<!DOCTYPE html>
<html lang="en">
<head>
<meta charset="utf-8">
<title>Glassvela – Custom Cut Mirror Frames</title>
<link href="https://fonts.googleapis.com/css2?family=Lato:wght@300;400;700&display=swap" rel="stylesheet">
<style>
:root{
  --purple:#c39bc9;
  --purple-dark:#b084b8;
  --teal:#8fc1c1;
  --ink:#333333;
  --muted:#666666;
  --white:#ffffff;
  --stage:#ececec;
}
*{box-sizing:border-box;margin:0;padding:0}
html,body{width:1200px;height:1200px;overflow:hidden}
body{background:var(--stage);font-family:'Lato',sans-serif;color:var(--ink)}
.page{position:absolute;left:284px;top:0;width:632px;height:1200px;background:var(--white);box-shadow:0 0 24px rgba(0,0,0,.12)}
.abs{position:absolute}
.promo-bar{left:0;top:0;width:632px;height:20px;background:var(--purple);color:var(--white);font-size:7px;font-weight:700;text-align:center;line-height:20px}
.utility-bar{left:0;top:20px;width:632px;height:19px;border-bottom:1px solid #ddd;font-size:5px;line-height:19px}
.utility-bar .left{position:absolute;left:46px;color:var(--teal);font-weight:700}
.utility-bar .left span{margin-right:14px}
.utility-bar .right{position:absolute;right:46px;color:var(--ink);font-weight:700}
.utility-bar .right span{margin-left:12px}
.cart-count{display:inline-block;width:8px;height:8px;border-radius:50%;background:var(--teal);color:#fff;text-align:center;line-height:8px;font-size:5px;margin-left:2px}
.brand{left:0;width:632px;text-align:center}
.brand-name{display:inline-flex;align-items:center;gap:6px;font-size:22px;font-weight:400;color:var(--ink)}
.brand-mark{width:10px;height:10px;background:var(--purple)}
.main-nav{left:0;top:108px;width:632px;text-align:center;font-size:6.5px;font-weight:700}
.main-nav a{color:var(--teal);text-decoration:none;margin:0 6px}
.main-nav a:nth-child(n+4){color:var(--purple)}
.hero{left:46px;top:124px;width:540px;height:231px;background:linear-gradient(90deg,#e9e2d6 0%,#d8c8b3 35%,#c89c72 60%,#d99a4a 100%)}
.hero-panel{left:182px;top:207px;width:268px;height:90px;background:rgba(240,200,160,.55);text-align:center;padding-top:14px}
.hero-panel h1{font-size:13px;font-weight:400;color:#2b2b2b;line-height:15px}
.hero-panel h1 span{display:block;font-size:12.5px}
.btn{display:block;background:var(--teal);color:var(--white);font-weight:700;text-align:center;text-decoration:none}
.hero-panel .btn{width:80px;height:16px;line-height:16px;font-size:6px;margin:16px auto 0}
.video{left:46px;top:364px;width:313px;height:201px;background:linear-gradient(135deg,#3a3b4a 0%,#6e6670 45%,#b9a29a 80%,#8a7b78 100%)}
.play{left:127px;top:81px;width:38px;height:38px;border-radius:50%;background:rgba(255,255,255,.35)}
.how{left:364px;top:364px;width:222px;height:201px;background:var(--purple);color:var(--white);padding:6px 6px 0 6px}
.how h2{font-size:13px;font-weight:700;margin-bottom:8px}
.how ul{list-style:none}
.how li{font-size:9.5px;height:16.2px;display:flex;align-items:center;gap:4px}
.tick{width:8px;height:8px;background:var(--white);flex:none}
.how .btn{position:absolute;left:6px;top:168px;width:210px;height:27px;line-height:27px;font-size:7.5px}
.section-title{left:46px;width:540px;display:flex;align-items:center;gap:6px;color:var(--purple);font-size:13px;font-weight:700;white-space:nowrap}
.section-title::before,.section-title::after{content:"";flex:1;height:2px;background:var(--purple)}
.card{width:131px;height:116px;border:1.5px solid var(--purple);background:var(--white)}
.card .thumb{height:85px;background:#efe8dc}
.card .label{position:absolute;left:0;top:85px;width:99px;height:28px;background:var(--purple);color:var(--white);padding:4px 4px}
.card .label b{display:block;font-size:7.5px;font-weight:700}
.card .label small{display:block;font-size:4.5px;margin-top:2px}
.card .cart{position:absolute;left:99px;top:85px;width:29px;height:28px;background:var(--teal);display:flex;align-items:center;justify-content:center}
.quote{top:962px;width:176px;height:79px;border:1.5px solid var(--purple);padding:13px 10px 0 24px;font-size:5.2px;line-height:7px;color:var(--ink)}
.quote .mark{position:absolute;font-size:18px;color:var(--teal);font-weight:700;line-height:18px}
.quote .open{left:7px;top:3px}
.quote .close{right:8px;bottom:2px}
.quote .who{margin-top:6px;color:var(--purple);font-weight:700}
.quote .stars{color:var(--teal);margin-left:8px;letter-spacing:1px;font-size:6px}
.wide-btn{left:228px;width:176px;height:26px;line-height:26px;font-size:7.5px}
.footer-bar{left:0;top:1179px;width:632px;height:21px;background:var(--purple);color:var(--white);font-size:6px;text-align:center;line-height:21px}
</style>
</head>
<body>
<div class="page">
  <div class="abs promo-bar">Happy easter! 15% off on all frames, all month long! Use code: HAPPY15</div>
  <div class="abs utility-bar">
    <div class="left"><span>● Sales and Promotions</span><span>☏ (555) 014-2290</span></div>
    <div class="right"><span>● Sign in</span><span>● My Cart <i class="cart-count">2</i></span></div>
  </div>

  <div class="abs brand" style="top:66px"><span class="brand-name"><i class="brand-mark"></i>Glassvela</span></div>
  <nav class="abs main-nav"><a>Shop</a><a>How it works</a><a>Testimonials</a><a>Featured Products</a><a>Before and After</a></nav>

  <div class="abs hero" role="img" aria-label="Photo of a smiling woman looking into a framed bathroom mirror"></div>
  <div class="abs hero-panel">
    <h1>FRAME ANY MIRROR IN YOUR HOUSE<span>with an elegant custom cut frame</span></h1>
    <a class="btn">SHOP NOW</a>
  </div>

  <div class="abs video" role="img" aria-label="Video still of a woman assembling a mirror frame on a kitchen counter">
    <svg class="abs play" viewBox="0 0 38 38"><polygon points="15,12 26,19 15,26" fill="#555"/></svg>
  </div>
  <div class="abs how">
    <h2>How it Works</h2>
    <ul>
      <li><i class="tick"></i>DIY mirror framing kit</li>
      <li><i class="tick"></i>Install with mirror still on wall</li>
      <li><i class="tick"></i>Style selections to match any home decor</li>
      <li><i class="tick"></i>DIY Install within minutes</li>
      <li><i class="tick"></i>Beveled Mirrors? No problem!</li>
      <li><i class="tick"></i>Guaranteed to fit any mirror, any size</li>
      <li><i class="tick"></i>Extends beyond mirror to hide ugly edges</li>
      <li><i class="tick"></i>100% Satisfaction Guarantee</li>
    </ul>
    <a class="btn">VIEW BEFORE &amp; AFTER GALLERY</a>
  </div>

  <div class="abs section-title" style="top:586px">Featured Products</div>

  <div class="abs card" style="left:46px;top:618px"><div class="thumb" role="img" aria-label="Silver frame sample" style="background:linear-gradient(135deg,#c9d3d3 55%,#8d8776 60%,#efe8dc 75%)"></div><div class="label"><b>Contemporary Silver</b><small>Modern Look</small></div><div class="cart"><svg width="11" height="10" viewBox="0 0 11 10"><path d="M0 1h2l1.5 5h6l1-4H3" fill="none" stroke="#fff" stroke-width="1.4"/><circle cx="4" cy="8.5" r="1" fill="#fff"/><circle cx="8.5" cy="8.5" r="1" fill="#fff"/></svg></div></div>
  <div class="abs card" style="left:183px;top:618px"><div class="thumb" role="img" aria-label="Bronze frame sample" style="background:linear-gradient(135deg,#e8e6e3 55%,#7a4a2e 60%,#efe8dc 75%)"></div><div class="label"><b>Harbor Bronze</b><small>Elegant Look</small></div><div class="cart"><svg width="11" height="10" viewBox="0 0 11 10"><path d="M0 1h2l1.5 5h6l1-4H3" fill="none" stroke="#fff" stroke-width="1.4"/><circle cx="4" cy="8.5" r="1" fill="#fff"/><circle cx="8.5" cy="8.5" r="1" fill="#fff"/></svg></div></div>
  <div class="abs card" style="left:319px;top:618px"><div class="thumb" role="img" aria-label="Black silver frame sample" style="background:linear-gradient(135deg,#e6e6e4 55%,#222 60%,#efe8dc 75%)"></div><div class="label"><b>Harbor Black Silver</b><small>Versatile Look</small></div><div class="cart"><svg width="11" height="10" viewBox="0 0 11 10"><path d="M0 1h2l1.5 5h6l1-4H3" fill="none" stroke="#fff" stroke-width="1.4"/><circle cx="4" cy="8.5" r="1" fill="#fff"/><circle cx="8.5" cy="8.5" r="1" fill="#fff"/></svg></div></div>
  <div class="abs card" style="left:456px;top:618px"><div class="thumb" role="img" aria-label="Black silver frame sample" style="background:linear-gradient(135deg,#e6e6e4 55%,#222 60%,#efe8dc 75%)"></div><div class="label"><b>Harbor Black Silver</b><small>Versatile Look</small></div><div class="cart"><svg width="11" height="10" viewBox="0 0 11 10"><path d="M0 1h2l1.5 5h6l1-4H3" fill="none" stroke="#fff" stroke-width="1.4"/><circle cx="4" cy="8.5" r="1" fill="#fff"/><circle cx="8.5" cy="8.5" r="1" fill="#fff"/></svg></div></div>

  <div class="abs card" style="left:46px;top:743px"><div class="thumb" role="img" aria-label="Java wood frame sample" style="background:linear-gradient(45deg,#efe8dc 25%,#6e3b22 30%,#8a5030 45%,#fff 50%)"></div><div class="label"><b>Linden Java</b><small>Modern Look</small></div><div class="cart"><svg width="11" height="10" viewBox="0 0 11 10"><path d="M0 1h2l1.5 5h6l1-4H3" fill="none" stroke="#fff" stroke-width="1.4"/><circle cx="4" cy="8.5" r="1" fill="#fff"/><circle cx="8.5" cy="8.5" r="1" fill="#fff"/></svg></div></div>
  <div class="abs card" style="left:183px;top:743px"><div class="thumb" role="img" aria-label="Silver frame sample" style="background:linear-gradient(45deg,#efe8dc 25%,#bdbdbd 30%,#d7d5d2 45%,#cfc9c2 50%)"></div><div class="label"><b>Simply Silver</b><small>Sleek &amp; Simple Look</small></div><div class="cart"><svg width="11" height="10" viewBox="0 0 11 10"><path d="M0 1h2l1.5 5h6l1-4H3" fill="none" stroke="#fff" stroke-width="1.4"/><circle cx="4" cy="8.5" r="1" fill="#fff"/><circle cx="8.5" cy="8.5" r="1" fill="#fff"/></svg></div></div>
  <div class="abs card" style="left:319px;top:743px"><div class="thumb" role="img" aria-label="Dark ornate frame sample" style="background:linear-gradient(45deg,#efe8dc 22%,#2b2b2e 28%,#3c3c40 45%,#dfe4e4 50%)"></div><div class="label"><b>Tuscan Bronze</b><small>Olde World Look</small></div><div class="cart"><svg width="11" height="10" viewBox="0 0 11 10"><path d="M0 1h2l1.5 5h6l1-4H3" fill="none" stroke="#fff" stroke-width="1.4"/><circle cx="4" cy="8.5" r="1" fill="#fff"/><circle cx="8.5" cy="8.5" r="1" fill="#fff"/></svg></div></div>
  <div class="abs card" style="left:456px;top:743px"><div class="thumb" role="img" aria-label="Dark ornate frame sample" style="background:linear-gradient(45deg,#efe8dc 22%,#2b2b2e 28%,#3c3c40 45%,#dfe4e4 50%)"></div><div class="label"><b>Tuscan Bronze</b><small>Olde World Look</small></div><div class="cart"><svg width="11" height="10" viewBox="0 0 11 10"><path d="M0 1h2l1.5 5h6l1-4H3" fill="none" stroke="#fff" stroke-width="1.4"/><circle cx="4" cy="8.5" r="1" fill="#fff"/><circle cx="8.5" cy="8.5" r="1" fill="#fff"/></svg></div></div>

  <a class="abs btn wide-btn" style="top:882px">SHOP ALL FRAMES</a>

  <div class="abs section-title" style="top:929px">What Our Customers Are Saying</div>

  <div class="abs quote" style="left:46px"><span class="mark open">"</span>Great product and great service! Adding frames to our mirrors made all the difference in how the master bath looks. You can't beat Glassvela for the money!<div class="who">Dana R., Encinitas, Ca<span class="stars">★★★★★</span></div><span class="mark close">"</span></div>
  <div class="abs quote" style="left:228px"><span class="mark open">"</span>We were so happy with the first two frames we purchased; we purchased a frame for our other bathroom. I would highly recommend this company.<div class="who">Marta S., Temecula, Ca<span class="stars">★★★★★</span></div><span class="mark close">"</span></div>
  <div class="abs quote" style="left:410px"><span class="mark open">"</span>I did my three bathrooms and couldn't be happier, what a difference the new frames made! Do yourself a favor and frame your mirrors, you'll be happy you did.<div class="who">Irene P., Lafayette, Ca<span class="stars">★★★★★</span></div><span class="mark close">"</span></div>

  <a class="abs btn wide-btn" style="top:1059px">GET FREE SAMPLE CODE</a>

  <div class="abs brand" style="top:1124px"><span class="brand-name"><i class="brand-mark"></i>Glassvela</span></div>

  <div class="abs footer-bar">COPYRIGHT © 2019. <b>Glassvela</b> | Custom Cut Mirror Frames</div>
</div>
</body>
</html>
```